Business card design for Tolvin Waste

I would like double-sided business cards for myself and my partner that includes our logo and the existing colour scheme. We provide waste and environmental services to customers in the motor-vehicle and engineering industries.

```html
<!DOCTYPE html>
<html lang="en">
<head>
<meta charset="utf-8">
<title>Tolvin Waste — Business Card</title>
<link rel="stylesheet" href="https://fonts.googleapis.com/css2?family=Roboto:wght@400;500;700&display=swap">
<style>
  :root {
    --stage: #2a2d30;
    --green-main: #6aac3f;
    --green-light: #b5d443;
    --green-text: #6fb43c;
    --ink: #3e4043;
    --paper: #f7f7f5;
    --rule: #6b6d70;
  }
  * { box-sizing: border-box; margin: 0; padding: 0; }
  html, body { width: 1200px; height: 900px; overflow: hidden; }
  body {
    background: var(--stage);
    font-family: "Roboto", Arial, sans-serif;
    display: flex;
    flex-direction: column;
    align-items: center;
    justify-content: center;
    gap: 40px;
  }
  .card {
    position: relative;
    width: 720px;
    height: 410px;
    border-radius: 26px;
    overflow: hidden;
  }
  /* Front */
  .card--front { background: var(--green-main); }
  .front-arcs { position: absolute; inset: 0; }
  .front-brand {
    position: absolute; inset: 0;
    display: flex; align-items: center; justify-content: center; gap: 22px;
  }
  .brand-dot {
    width: 64px; height: 64px; border-radius: 50%;
    background: #ffffff;
  }
  .front-brand .brand-name {
    font-size: 64px; font-weight: 700; color: #ffffff; letter-spacing: 1px;
  }
  /* Back */
  .card--back { background: var(--paper); color: var(--ink); }
  .holder { position: absolute; left: 50px; top: 42px; }
  .holder-name {
    color: var(--green-text); font-size: 30px; font-weight: 500;
    text-transform: uppercase; letter-spacing: 0.5px;
  }
  .holder-role { font-size: 20px; font-weight: 500; margin-top: 2px; }
  .rule-h {
    position: absolute; left: 50px; right: 40px; top: 135px;
    height: 1.5px; background: var(--rule);
  }
  .rule-v {
    position: absolute; left: 400px; top: 250px;
    width: 1.5px; height: 110px; background: var(--rule);
  }
  .contacts { position: absolute; left: 50px; top: 168px; list-style: none; }
  .contacts li {
    display: flex; align-items: center; gap: 12px;
    font-size: 19px; margin-bottom: 12px;
  }
  .icon {
    width: 26px; height: 26px; border-radius: 50%;
    background: var(--green-main);
    display: flex; align-items: center; justify-content: center;
  }
  .back-brand {
    position: absolute; right: 48px; top: 165px;
    display: flex; align-items: center; gap: 14px;
  }
  .back-brand .brand-dot { width: 44px; height: 44px; background: var(--green-text); }
  .back-brand .brand-name { font-size: 44px; font-weight: 700; color: var(--ink); }
  .address {
    position: absolute; left: 430px; top: 280px;
    font-size: 19px; line-height: 1.45;
  }
</style>
</head>
<body>
  <section class="card card--front">
    <svg class="front-arcs" viewBox="0 0 720 410" preserveAspectRatio="none" aria-hidden="true">
      <path d="M470 0 Q520 230 720 300 L720 0 Z" fill="var(--green-light)"/>
      <path d="M0 130 Q230 160 270 410 L0 410 Z" fill="var(--green-light)"/>
    </svg>
    <div class="front-brand">
      <span class="brand-dot"></span>
      <span class="brand-name">Tolvin Waste</span>
    </div>
  </section>

  <section class="card card--back">
    <div class="holder">
      <p class="holder-name">Marcus Halden</p>
      <p class="holder-role">Partner</p>
    </div>
    <div class="rule-h"></div>

    <ul class="contacts">
      <li>
        <span class="icon"><svg width="14" height="14" viewBox="0 0 24 24"><path fill="#fff" d="M6.6 10.8a15 15 0 0 0 6.6 6.6l2.2-2.2c.3-.3.7-.4 1-.2 1.1.4 2.3.6 3.6.6.6 0 1 .4 1 1V20c0 .6-.4 1-1 1A17 17 0 0 1 3 4c0-.6.4-1 1-1h3.5c.6 0 1 .4 1 1 0 1.3.2 2.5.6 3.6.1.3 0 .7-.2 1z"/></svg></span>
        555 014 2290
      </li>
      <li>
        <span class="icon"><svg width="14" height="14" viewBox="0 0 24 24"><path fill="#fff" d="M3 5h18v14H3z"/><path d="M3 5l9 7 9-7" fill="none" stroke="#6aac3f" stroke-width="2"/></svg></span>
        email@TolvinWaste.com
      </li>
      <li>
        <span class="icon"><svg width="14" height="14" viewBox="0 0 24 24"><circle cx="12" cy="12" r="9" fill="none" stroke="#fff" stroke-width="2"/><path d="M3 12h18M12 3c3 3 3 15 0 18M12 3c-3 3-3 15 0 18" fill="none" stroke="#fff" stroke-width="1.6"/></svg></span>
        www.TolvinWaste.com
      </li>
    </ul>

    <div class="back-brand">
      <span class="brand-dot"></span>
      <span class="brand-name">Tolvin Waste</span>
    </div>

    <div class="rule-v"></div>
    <address class="address" style="font-style:normal">
      412 Alder Rd.<br>Brookhaven, NJ 08012
    </address>
  </section>
</body>
</html>
```